Hello everyone,
I need someone to design a Business Card for my new company. It's called Norvakeep and we give procurement services of Chilean Salmon and Seafood in General. More specifically we are purchasing agents, quality inspectors and we help with general papework and logistics. Maybe in the future can open to some agriculture items such as Meat, Dairy Products and Fruits.
All this focused in international clients that cannot have the support they need when buying items from Chile.
A main concept is reliability.

Thank you in advance.

Esteban.

Target Market(s)

Salmon and Seafood Importers from all world.

Industry/Entity Type

Business

Contact Information for Business Card

The Name: Esteban Ruiz Pardo
My Mobile: +56 9 47316258
My Location: Puerto varas, Chile

Font styles to use
Serif
Sans Serif

Requirements
Must have
• The company name and a logo.
Nice to have
• Some full color on the back side.
Should not have
• No modern shapes. Just a rectangular business card. Remember that has to be accepted by a lot of different cultures, even senior Japanese clients.

```html
<!DOCTYPE html>
<html lang="en">
<head>
<meta charset="utf-8">
<title>Norvakeep – Business Card</title>
<link rel="stylesheet" href="https://fonts.googleapis.com/css2?family=Marcellus+SC&display=swap">
<style>
  :root {
    --page-bg: #e6e7e9;
    --card-white: #ffffff;
    --card-fade: #eceded;
    --brand-blue: #0b96d6;
    --band-grey: #9a9b9d;
    --ink: #3a3a3c;
    --icon-dark: #3c3d40;
  }
  * { box-sizing: border-box; margin: 0; padding: 0; }
  html, body {
    width: 1200px; height: 900px; overflow: hidden;
    background: var(--page-bg);
  }
  .card {
    position: absolute; left: 110px; top: 170px;
    width: 980px; height: 560px;
    overflow: hidden;
    background: radial-gradient(ellipse at 55% 35%, var(--card-white) 0%, var(--card-fade) 100%);
    box-shadow: 0 12px 30px rgba(0,0,0,0.18);
    font-family: "Marcellus SC", serif;
    color: var(--ink);
  }
  .band { position: absolute; left: 0; width: 100%; }
  .band--grey { top: 438px; height: 34px; background: var(--band-grey); }
  .band--blue { top: 480px; height: 80px; background: var(--brand-blue); }

  .brand {
    position: absolute; left: 190px; top: 62px;
    display: flex; align-items: center; gap: 22px;
  }
  .brand__mark {
    width: 34px; height: 34px; background: var(--brand-blue);
  }
  .brand__name {
    font-size: 84px; letter-spacing: 2px; line-height: 1;
    color: var(--brand-blue); font-weight: 400;
  }
  .holder {
    position: absolute; right: 560px; top: 214px;
    text-align: right; letter-spacing: 1.5px;
  }
  .holder__name { font-size: 25px; letter-spacing: 2.5px; line-height: 32px; }
  .holder__role { font-size: 20px; line-height: 28px; }
  .holder__address { font-size: 20px; line-height: 28px; margin-top: 20px; }
  .divider {
    position: absolute; left: 436px; top: 218px;
    width: 1px; height: 166px; background: var(--ink);
  }
  .contacts {
    position: absolute; left: 452px; top: 216px;
    list-style: none; font-size: 21px; letter-spacing: 1.5px;
  }
  .contacts li { display: flex; align-items: center; height: 31px; white-space: nowrap; }
  .contacts svg { width: 20px; height: 20px; margin-right: 10px; flex: none; }
</style>
</head>
<body>
  <div class="card">
    <div class="band band--grey"></div>
    <div class="band band--blue"></div>

    <div class="brand">
      <span class="brand__mark"></span>
      <span class="brand__name">Norvakeep</span>
    </div>

    <div class="holder">
      <p class="holder__name">Esteban Ruiz Pardo</p>
      <p class="holder__role">Owner / C.E.O</p>
      <p class="holder__address">Of. 302, Edif. Alto,<br>Puerto Varas</p>
    </div>

    <div class="divider"></div>

    <ul class="contacts">
      <li>
        <svg viewBox="0 0 20 20"><circle cx="10" cy="10" r="10" fill="var(--icon-dark)"/><path d="M6,5 L8,5 L9,8 L8,9 C8.6,10.6 9.4,11.4 11,12 L12,11 L15,12 L15,14 C10,15 5,10 6,5 Z" fill="#fff"/></svg>
        +56 9 47316258
      </li>
      <li>
        <svg viewBox="0 0 20 20"><circle cx="10" cy="10" r="10" fill="var(--icon-dark)"/><rect x="7" y="4" width="6" height="12" rx="1" fill="#fff"/><rect x="8" y="5.5" width="4" height="7" fill="var(--icon-dark)"/></svg>
        +56 65 2481937
      </li>
      <li>
        <svg viewBox="0 0 20 20"><circle cx="10" cy="10" r="10" fill="var(--icon-dark)"/><rect x="5" y="8" width="10" height="7" rx="1" fill="#fff"/><rect x="7" y="4.5" width="6" height="4" fill="#fff"/></svg>
        +56 65 2481938
      </li>
      <li>
        <svg viewBox="0 0 20 20"><circle cx="10" cy="10" r="10" fill="var(--icon-dark)"/><rect x="4.5" y="6" width="11" height="8" fill="#fff"/><path d="M4.5,6 L10,10.5 L15.5,6" fill="none" stroke="var(--icon-dark)" stroke-width="1.2"/></svg>
        esteban@norvakeep.cl
      </li>
      <li>
        <svg viewBox="0 0 20 20"><circle cx="10" cy="10" r="10" fill="var(--icon-dark)"/><circle cx="10" cy="10" r="5.5" fill="none" stroke="#fff" stroke-width="1.2"/><ellipse cx="10" cy="10" rx="2.3" ry="5.5" fill="none" stroke="#fff" stroke-width="1"/><line x1="4.5" y1="10" x2="15.5" y2="10" stroke="#fff" stroke-width="1"/></svg>
        www.norvakeep.cl
      </li>
    </ul>
  </div>
</body>
</html>
```